Welcome Card

We are a privately owned waste removal company. We need a postcard designed to insert into a card that we send out to new customers. This card will list some of our company policies. Our company is known for having "the purplest trucks", so we must incorporate the color purple.

```html
<!DOCTYPE html>
<html lang="en">
<head>
<meta charset="utf-8">
<title>Summit Ridge Waste – Welcome Card</title>
<link href="https://fonts.googleapis.com/css2?family=Source+Sans+3:wght@400;600;700&display=swap" rel="stylesheet">
<style>
  :root {
    --page: #eeebe6;
    --purple-deep: #2e1653;
    --purple: #4b2a82;
    --purple-mid: #6a3fa8;
    --lilac-band: rgba(226, 214, 243, 0.78);
    --ink: #1b1b1b;
    --white: #ffffff;
    --shadow: 0 6px 14px rgba(0, 0, 0, 0.35);
  }
  * { box-sizing: border-box; margin: 0; padding: 0; }
  html, body {
    width: 1200px; height: 769px; overflow: hidden;
    background: var(--page);
    font-family: "Source Sans 3", "Myriad Pro", sans-serif;
  }
  .stage { position: relative; width: 1200px; height: 769px; }

  .card {
    position: absolute;
    width: 419px; height: 543px;
    box-shadow: var(--shadow);
    overflow: hidden;
    background:
      radial-gradient(ellipse 70% 40% at 80% 62%, rgba(190, 150, 235, 0.55), transparent 70%),
      linear-gradient(160deg, var(--purple-deep) 0%, var(--purple) 35%, var(--purple-mid) 62%, var(--purple-deep) 100%);
  }
  .card--front { left: 242px; top: 47px; }
  .card--back  { left: 710px; top: 179px; width: 420px; }

  /* Brand block */
  .brand {
    background: var(--white);
    display: flex; flex-direction: column; align-items: center; justify-content: center;
    text-align: center;
  }
  .brand__mark {
    width: 22px; height: 22px; border-radius: 50%;
    background: var(--purple);
    margin-bottom: 12px;
  }
  .brand__name {
    color: var(--purple);
    font-weight: 700;
    text-transform: uppercase;
    line-height: 1.05;
  }
  .brand__rule { height: 2px; background: var(--purple); margin: 8px 0 7px; }
  .brand__tagline { font-weight: 600; line-height: 1.2; color: var(--ink); }

  .card--front .brand {
    position: absolute; left: 88px; top: 0; width: 244px; height: 256px;
    padding: 18px 12px;
  }
  .card--front .brand__name { font-size: 27px; }
  .card--front .brand__rule { width: 180px; }
  .card--front .brand__tagline { font-size: 17px; }

  .welcome-band {
    position: absolute; left: 0; top: 377px; width: 100%; height: 84px;
    background: var(--lilac-band);
    display: flex; align-items: center; justify-content: center;
    text-align: center;
    font-size: 20px; font-weight: 600; line-height: 1.3; color: var(--ink);
  }
  .site-url {
    position: absolute; left: 0; top: 494px; width: 100%;
    text-align: center; color: var(--white);
    font-size: 18px; font-weight: 700;
  }

  /* Back */
  .card--back .brand { height: 128px; padding: 8px; }
  .card--back .brand__mark { width: 12px; height: 12px; margin-bottom: 5px; }
  .card--back .brand__name { font-size: 14px; }
  .card--back .brand__rule { width: 96px; height: 1.5px; margin: 4px 0 3px; }
  .card--back .brand__tagline { font-size: 9.5px; }

  .back-title {
    height: 47px;
    display: flex; align-items: center; justify-content: center; text-align: center;
    color: var(--white); font-size: 14px; font-weight: 700; line-height: 1.15;
  }
  .policies {
    height: 317px;
    background: rgba(200, 175, 235, 0.28);
    padding: 12px 18px 0 14px;
    color: var(--white);
    font-size: 11.8px; line-height: 1.35;
  }
  .policies ul { list-style: none; }
  .policies li { margin-bottom: 10px; }
  .policies li::before { content: "\2022"; margin-right: 5px; }
  .policies .blank { display: inline-block; width: 110px; border-bottom: 1px solid var(--white); }
  .policies .contact { text-align: right; margin-top: 14px; }
  .policies .contact strong { margin-left: 4px; }
  .social {
    height: 51px;
    display: flex; justify-content: flex-end; align-items: center; gap: 8px;
    padding-right: 16px;
  }
  .social__dot { width: 24px; height: 24px; border-radius: 50%; background: rgba(255,255,255,0.8); }
</style>
</head>
<body>
<main class="stage">

  <section class="card card--front">
    <div class="brand">
      <div class="brand__mark"></div>
      <div class="brand__name">Summit Ridge<br>Waste</div>
      <div class="brand__rule"></div>
      <p class="brand__tagline">Fair rates. Friendly crews.<br>Bold fleet.</p>
    </div>
    <div class="welcome-band">Thank you for signing up for service with<br>Summit Ridge Waste</div>
    <p class="site-url">www.summitridgewaste.com</p>
  </section>

  <section class="card card--back">
    <div class="brand">
      <div class="brand__mark"></div>
      <div class="brand__name">Summit Ridge<br>Waste</div>
      <div class="brand__rule"></div>
      <p class="brand__tagline">Fair rates. Friendly crews.<br>Bold fleet.</p>
    </div>
    <h2 class="back-title">Thank you for signing up for service with<br>Summit Ridge Waste</h2>
    <div class="policies">
      <ul>
        <li>Please remember to have your trash out for pickup by<br>7AM on <span class="blank"></span>. We are only in your area once a week and cannot send a truck back if you missed our truck.</li>
        <li>We can provide removal of furniture, appliances, construction and remodel materials for an <strong>extra charge</strong>. Please call our office to make arrangements.</li>
        <li>Late fees are assessed to accounts that have not been paid within 25 days of billing. We charge a restart fee once a suspended account is restarted.</li>
        <li>Not responsible for damage to trash cans.</li>
        <li>Holiday Service - call our office for information on Holiday Schedules.</li>
        <li>Sign up for our newsletter at <strong>www.summitridgewaste.com</strong></li>
      </ul>
      <p class="contact">Any questions, please call our office at: <strong>555-0147</strong></p>
    </div>
    <div class="social">
      <span class="social__dot"></span>
      <span class="social__dot"></span>
    </div>
  </section>

</main>
</body>
</html>
```